Membership Webpage Revamp

I am needing to redo two of the pages on our current wordpress site
http://brightoakclinic.com/thrivenow-membership/
and
http://brightoakclinic.com/medical-fitness/
For the medical fitness page we will need a sub navigation I guess like we have on our services pages but I am open to ideas
http://brightoakclinic.com/ourservices/functional-medicine/
One On One
Group Sessions - Class Schedule
Trainer Page
Program Details
Will need to use the plugin from flexroster for the class schedule on the group sessions page
We have redone what is included in our memberships and needing to update our site to reflect the changes.
I am wanting the layout to be as clean as possible and make it as easy to understand as possible for users.
I am wanting icons for the different membership tiers to represent the different categories.
It should show the main 3 categories
$20 Core Start = Basic
$60 Core Boost = Goal Specific - Trim Path (Weight Loss), Ease Motion, Stay Bright Stay Young (Antiaging/Hormone)
$150 Core Renewed = Peak 2 Go (Ultimate Health Prevention)
If a user then clicks on Core Boost then it would give the option of the 3 programs under that category.
Trim Path (Weight Loss), Ease Motion, Stay Bright Stay Young (Antiaging/Hormone)
Then at the bottom can have the add on package for Core Power
Core Power = Med Fit add on to our memberships
Or another way the layout could be would be to have Core Renewed = Peak 2 Go (Ultimate Health Prevention) package at the top by itself
Then the 3 middle options Core Boost = Goal Specific - Trim Path (Weight Loss), Ease Motion, Stay Bright Stay Young (Antiaging/Hormone) and then the basic option at the bottom
Potentially I would like to have a checkbox comparison of the main 3 categories Core Start, Core Boost, Core Renewed for the following areas
Online Benefits
Testing Discounts
Therapy Discounts
Procedure Discounts
The new text content for the membership page is attached
Would like a graphic that illustrates that all the features of Core Start are in Core Boost and that for Core Renewed has all the features of both Core Start and Core Boost
Wanting a graphic to illustrate the stages of lifestyle change and also to redo the example mock up I did of our services and our 3 tiers Functional Medicine, Medical Fitness, and Sports and Orthopedics.
I am wanting a playlist of the videos of our services that would be included in each package in the popup of the details of the package or that when they click on a service that a video will popup with the clip of the service.

```html
<!DOCTYPE html>
<html lang="en">
<head>
<meta charset="utf-8">
<title>Bright Oak Clinic – ThriveNow Membership</title>
<link href="https://fonts.googleapis.com/css2?family=Open+Sans:wght@400;600;700;800&display=swap" rel="stylesheet">
<style>
:root{
  --green:#8dc63f;
  --green-dark:#7ab32e;
  --blue:#2a9fd8;
  --blue-dark:#1f8cc4;
  --red:#e0262b;
  --ink:#333;
  --muted:#777;
  --line:#dcdcdc;
  --soft:#f4f5f7;
  --footer:#222;
  --white:#fff;
}
*{box-sizing:border-box;margin:0;padding:0}
html,body{width:1200px;height:4027px;overflow:hidden}
body{font-family:"Open Sans",Arial,sans-serif;color:var(--ink);background:var(--white);position:relative}
.abs{position:absolute}
section,header,footer,nav{position:absolute;left:0;width:1200px}

.topbar{top:0;height:48px;background:var(--blue);color:#fff;font-size:14px}
.topbar .info{position:absolute;left:100px;top:14px;display:flex;gap:30px}
.topbar .portal{position:absolute;right:100px;top:6px;background:var(--green);padding:9px 26px;font-size:13px;font-weight:600}

.masthead{top:48px;height:108px}
.brand{position:absolute;left:88px;top:30px;display:flex;align-items:center;gap:12px}
.brand .dot{width:40px;height:40px;border-radius:50%;background:var(--green)}
.brand .name{font-size:30px;font-weight:700;color:var(--blue)}
.cta-pill{position:absolute;left:636px;top:28px;width:246px;height:50px;border-radius:25px;background:var(--green);color:#fff;font-size:13px;font-weight:700;display:flex;align-items:center;justify-content:center}
.call{position:absolute;left:916px;top:26px;display:flex;align-items:center;gap:14px}
.call .ico{width:52px;height:52px;border-radius:50%;background:var(--blue);display:flex;align-items:center;justify-content:center}
.call small{display:block;font-size:13px;color:var(--muted)}
.call strong{font-size:24px;font-weight:600;color:var(--blue)}

.mainnav{top:156px;height:54px;background:var(--green);display:flex;justify-content:center;align-items:center;gap:22px}
.mainnav a{color:#fff;font-size:12.5px;font-weight:600;text-decoration:none}

.hero{top:210px;height:520px;background:linear-gradient(90deg,#eef2ee 0%,#f7f7f5 40%)}
.hero .photo{position:absolute;left:390px;top:0;width:810px;height:520px;background:linear-gradient(120deg,#e7e9df 0%,#d9c8b4 35%,#b9cf86 70%,#8aa84c 100%)}
.hero .copy{position:absolute;left:84px;top:168px}
.hero h1{font-size:44px;font-weight:800;color:var(--green);line-height:1.1}
.hero h2{font-size:31px;font-weight:700;color:var(--green);margin-top:4px}
.hero h3{font-size:26px;font-weight:600;color:var(--blue);margin-top:16px}
.hero .btn{display:inline-block;margin-top:34px;background:var(--green);color:#fff;font-size:13px;font-weight:700;padding:16px 32px;border-radius:26px}

.sec-title{position:absolute;left:0;width:1200px;text-align:center;font-size:28px;font-weight:700;color:var(--blue)}
.sec-title.green{color:var(--green)}
.sec-title.white{color:#fff}
.sec-sub{position:absolute;left:0;width:1200px;text-align:center;font-size:12px;color:var(--muted)}

.categories{top:730px;height:411px}
.cat{position:absolute;top:136px;width:300px;text-align:center}
.cat .badge{width:126px;height:126px;border-radius:50%;margin:0 auto;border:6px solid #dfeec9;display:flex;align-items:center;justify-content:center}
.cat .badge.g{background:var(--green)}
.cat .badge.b{background:var(--blue);border-color:#cfe7f6}
.cat .lvl{margin-top:14px;font-size:17px;font-weight:600}
.cat .price{font-size:15px;color:var(--green)}
.cat p{font-size:13px;line-height:1.6;color:#222}

.compare{top:1141px;height:449px;background:var(--soft)}
.cmp{position:absolute;left:107px;top:101px;width:875px;border-collapse:collapse;background:#fff}
.cmp th{background:var(--green);color:#fff;font-size:15px;font-weight:700;height:50px;border:1px solid #fff}
.cmp th.blank{background:transparent}
.cmp td{height:62px;border:1px solid var(--line);text-align:center;font-size:13px}
.cmp td.label{text-align:left;padding-left:20px;width:222px;color:#555}

.tiers{top:1590px;height:746px}
.oval{position:absolute;height:86px;border-radius:50%;border:5px solid #fff;box-shadow:0 0 0 2px var(--line);color:#fff;font-size:16px;font-weight:700;display:flex;align-items:center;justify-content:center}
.oval.b{background:var(--blue)}
.oval.g{background:var(--green)}
.card{position:absolute;color:#fff;padding:20px 16px;font-size:12px}
.card.b{background:var(--blue)}
.card.g{background:var(--green)}
.card li{list-style:none;margin-bottom:16px;padding-left:14px;position:relative}
.card li::before{content:"›";position:absolute;left:0;top:-2px}
.card::before{content:"";position:absolute;top:-14px;width:0;height:0;border-left:14px solid transparent;border-right:14px solid transparent;border-bottom:14px solid}
.card.b::before{border-bottom-color:var(--blue);left:140px}
.card.g::before{border-bottom-color:var(--green);left:150px}
.card.b.r::before{left:30px}
.hub{position:absolute;left:524px;top:130px;width:172px;height:172px;border-radius:50%;background:var(--green);border:6px solid #fff;box-shadow:0 0 0 2px var(--green);display:flex;align-items:center;justify-content:center;gap:8px;color:#fff;font-weight:700;font-size:20px}
.hub .dot{width:22px;height:22px;border-radius:50%;background:#fff}

.lifestyle{top:2336px;height:309px;background:var(--blue)}
.life{position:absolute;left:183px;top:91px;width:837px;border-collapse:collapse;background:#fff}
.life th{background:var(--green);color:#fff;font-size:13px;font-weight:600;height:49px;border-right:1px solid #fff}
.life td{border:1px solid var(--line);text-align:center;font-size:11px;color:#555}
.life tr.t td{height:62px}
.life tr.l td{height:67px;text-transform:uppercase}

.features{top:2645px;height:470px;overflow:hidden}

.faq{top:3115px;height:572px;background:var(--soft)}
.acc{position:absolute;left:263px;width:671px}
.acc .head{height:48px;display:flex;align-items:center;justify-content:space-between;padding:0 20px;font-size:14px;border:1px solid var(--line);background:#fff}
.acc .head.open{background:var(--green);color:#fff;border-color:var(--green);font-weight:600}
.acc .box{width:14px;height:14px;border:1.5px solid currentColor;position:relative}
.acc .box::after{content:"";position:absolute;left:3px;top:5px;width:5px;height:1.5px;background:currentColor}
.acc .ans{font-size:11.5px;color:var(--muted);line-height:1.7;padding:12px 20px}

.sitefoot{top:3687px;height:268px;background:var(--footer);color:#bbb}
.sitefoot .brand{left:158px;top:38px}
.sitefoot .brand .name{color:#fff;font-size:26px}
.social{position:absolute;left:94px;top:140px;display:flex;gap:18px}
.social span{width:40px;height:40px;border-radius:50%;background:#fff}
.sitefoot h4{color:#fff;font-size:17px;font-weight:600;position:absolute}
.hours{position:absolute;left:438px;top:80px;font-size:13px;line-height:22px}
.hours div{display:flex;width:240px;justify-content:space-between}
.touch{position:absolute;left:784px;top:80px;font-size:13px}
.touch div{display:flex;align-items:center;gap:12px;height:44px}
.copyright{position:absolute;left:0;width:1200px;top:3955px;height:72px;background:var(--blue);color:#fff;font-size:12px;display:flex;align-items:center;justify-content:center}
</style>
</head>
<body>

<div class="topbar">
  <div class="info"><span>⏱ Today's Working Hours : 8 am - 6 pm</span><span>✉ info@brightoakclinic.com</span></div>
  <div class="portal">PATIENT PORTAL</div>
</div>

<header class="masthead">
  <div class="brand"><span class="dot"></span><span class="name">Bright Oak Clinic</span></div>
  <div class="cta-pill">SCHEDULE AN APPOINTMENT</div>
  <div class="call">
    <div class="ico"><svg width="24" height="24" viewBox="0 0 24 24"><path fill="#fff" d="M6.6 10.8a15 15 0 0 0 6.6 6.6l2.2-2.2c.3-.3.7-.4 1-.2 1.1.4 2.3.6 3.6.6.6 0 1 .4 1 1V20c0 .6-.4 1-1 1A17 17 0 0 1 3 4c0-.6.4-1 1-1h3.5c.6 0 1 .4 1 1 0 1.3.2 2.5.6 3.6.1.3 0 .7-.2 1z"/></svg></div>
    <div><small>Call Us Now</small><strong>(555) 214-7730</strong></div>
  </div>
</header>

<nav class="mainnav">
  <a>HOME</a><a>START HERE</a><a>ABOUT</a><a>SERVICES</a><a>RESOURCES</a><a>FAQ</a><a>CURRENT PATIENTS</a><a>NEW PATIENTS</a><a>THRIVENOW MEMBERSHIP</a><a>MEDICAL FITNESS</a><a>BLOG</a><a>CONTACT</a>
</nav>

<section class="hero">
  <div class="photo" role="img" aria-label="Photo of a smiling family of four outdoors on green grass"></div>
  <div class="copy">
    <h1>NEW TO BRIGHT OAK</h1>
    <h2>FAMILY CLINIC</h2>
    <h3>LEARN MORE ABOUT US HERE</h3>
    <div class="btn">CLICK HERE TO START YOUR BRIGHT OAK LIFE</div>
  </div>
</section>

<section class="categories">
  <h2 class="sec-title" style="top:44px">OUR CATEGORIES</h2>
  <p class="sec-sub" style="top:90px">With insurance reimbursements going down, and expenses going up, we are implementing new opportunities</p>
  <div class="cat" style="left:107px">
    <div class="badge g"><svg width="60" height="60" viewBox="0 0 60 60" fill="none" stroke="#fff" stroke-width="3"><path d="M30 14a12 12 0 0 0-7 22v6h14v-6a12 12 0 0 0-7-22z"/><path d="M24 47h12M26 52h8M30 4v5M12 12l4 4M48 12l-4 4M6 28h5M49 28h5"/></svg></div>
    <div class="lvl" style="color:var(--green)">BASIC</div>
    <div class="price">$20 Core Start</div>
  </div>
  <div class="cat" style="left:450px">
    <div class="badge b"><svg width="64" height="64" viewBox="0 0 64 64" fill="none" stroke="#fff" stroke-width="3"><circle cx="30" cy="34" r="22"/><circle cx="30" cy="34" r="14"/><circle cx="30" cy="34" r="6"/><path d="M30 34L54 10M48 8l6 2 2 6"/></svg></div>
    <div class="lvl" style="color:var(--blue)">GOAL SPECIFIC</div>
    <div class="price" style="color:var(--blue)">$60 Core Boost</div>
    <p>Trim Path (Weight Loss), Ease Motion,<br>Stay Bright Stay Young (Antiaging/Hormone)</p>
  </div>
  <div class="cat" style="left:793px">
    <div class="badge g"><svg width="60" height="60" viewBox="0 0 60 60" fill="none" stroke="#fff" stroke-width="3"><circle cx="30" cy="15" r="6"/><path d="M16 26l14 4 14-4M30 30v12M22 54l8-12 8 12"/></svg></div>
    <div class="lvl" style="color:var(--green)">PEAK 2 GO</div>
    <div class="price">$150 Core Renewed</div>
    <p>(Ultimate Health Prevention)</p>
  </div>
</section>

<section class="compare">
  <h2 class="sec-title green" style="top:42px">CATEGORIES COMPARISON</h2>
  <table class="cmp">
    <tr><th class="blank"></th><th>CORE START</th><th>CORE BOOST</th><th>CORE RENEWED</th></tr>
    <tr><td class="label">ONLINE BENEFITS</td><td><svg width="28" height="28"><use href="#tick"/></svg></td><td><svg width="28" height="28"><use href="#tick"/></svg></td><td><svg width="28" height="28"><use href="#cross"/></svg></td></tr>
    <tr><td class="label">TESTING DISCOUNTS</td><td><svg width="28" height="28"><use href="#tick"/></svg></td><td><svg width="28" height="28"><use href="#cross"/></svg></td><td><svg width="28" height="28"><use href="#tick"/></svg></td></tr>
    <tr><td class="label">THERAPY DISCOUNTS</td><td><svg width="28" height="28"><use href="#cross"/></svg></td><td><svg width="28" height="28"><use href="#tick"/></svg></td><td><svg width="28" height="28"><use href="#cross"/></svg></td></tr>
    <tr><td class="label">PROCEDURE DISCOUNTS</td><td><svg width="28" height="28"><use href="#tick"/></svg></td><td><svg width="28" height="28"><use href="#cross"/></svg></td><td><svg width="28" height="28"><use href="#tick"/></svg></td></tr>
  </table>
</section>

<svg width="0" height="0" style="position:absolute">
  <defs>
    <symbol id="tick" viewBox="0 0 28 28"><circle cx="14" cy="14" r="13" fill="#5bb531"/><path d="M8 14l4 4 8-8" fill="none" stroke="#fff" stroke-width="3"/></symbol>
    <symbol id="cross" viewBox="0 0 28 28"><circle cx="14" cy="14" r="13" fill="#e0262b"/><path d="M9 9l10 10M19 9L9 19" stroke="#fff" stroke-width="3"/></symbol>
  </defs>
</svg>

<section class="tiers">
  <h2 class="sec-title" style="top:40px">OUR 3 TIERS SERVICES</h2>
  <p class="sec-sub" style="top:86px">With insurance reimbursements going down, and expenses going up, we are implementing new opportunities</p>
  <svg class="abs" style="left:0;top:0" width="1200" height="746">
    <path d="M560 280L330 370M610 308V390M660 280L900 370" stroke="#bbb" stroke-width="2" fill="none"/>
  </svg>
  <div class="hub"><span class="dot"></span>Bright Oak</div>
  <div class="oval b" style="left:196px;top:330px;width:236px">FUNCTIONAL MEDICINE</div>
  <div class="oval g" style="left:494px;top:392px;width:232px">MEDICAL FITNESS</div>
  <div class="oval b" style="left:792px;top:330px;width:236px">SPORTS &amp; ORTHOPEDICS</div>
  <ul class="card b" style="left:161px;top:445px;width:201px;height:242px">
    <li>Advanced Lab Testing</li><li>Hormone Optimization</li><li>Aesthetic Medicine</li><li>Allergy Testing</li><li>Oral Health</li><li>Integrative Family Medicine</li>
  </ul>
  <ul class="card g" style="left:510px;top:510px;width:202px;height:142px">
    <li>Fitness</li><li>Weight Loss</li><li>Nutrition</li><li>Personal Training</li>
  </ul>
  <ul class="card b r" style="left:827px;top:445px;width:204px;height:153px">
    <li>Manipulation</li><li>Non Surgical Regenerative</li><li>Injections</li><li>Acupuncture</li>
  </ul>
</section>

<section class="lifestyle">
  <h2 class="sec-title white" style="top:34px">LIFESTYLE</h2>
  <table class="life">
    <tr><th>Health Coach</th><th>Intro Period</th><th>Transition</th><th>Maintenance</th><th>Lifestyle Health&amp; Fitness</th></tr>
    <tr class="t"><td></td><td>0 ------------------------ 6mo</td><td>6mo ------------------- 1 Year</td><td>1Year ------------------ 3 Year</td><td></td></tr>
    <tr class="l"><td>Patient</td><td>Learning</td><td>Life</td><td>Emotional</td><td>Goal</td></tr>
  </table>
</section>

<section class="features">
  <h2 class="sec-title" style="top:40px">OUR FEATURES</h2>
  <p class="sec-sub" style="top:86px">With insurance reimbursements going down, and expenses going up, we are implementing new opportunities</p>
  <svg class="abs" style="left:410px;top:108px" width="380" height="360" viewBox="0 0 380 360">
    <circle cx="190" cy="180" r="176" fill="#8dc63f" stroke="#7ab32e" stroke-width="4"/>
    <circle cx="190" cy="220" r="130" fill="#2a9fd8" stroke="#fff" stroke-width="6"/>
    <circle cx="190" cy="300" r="46" fill="#fff"/>
    <text x="190" y="66" text-anchor="middle" fill="#fff" font-family="Open Sans, sans-serif" font-size="16" font-weight="600">CORE RENEWED</text>
    <text x="190" y="196" text-anchor="middle" fill="#fff" font-family="Open Sans, sans-serif" font-size="16" font-weight="600">CORE BOOST</text>
    <text x="190" y="295" text-anchor="middle" fill="#333" font-family="Open Sans, sans-serif" font-size="12">CORE</text>
    <text x="190" y="311" text-anchor="middle" fill="#333" font-family="Open Sans, sans-serif" font-size="12">START</text>
  </svg>
</section>

<section class="faq">
  <h2 class="sec-title" style="top:100px">OUR FAQ'S</h2>
  <p class="sec-sub" style="top:146px">With insurance reimbursements going down, and expenses going up, we are implementing new opportunities</p>
  <div class="acc" style="top:214px">
    <div class="head open">Can the online supplement discounts be applied to in office supplement?<span class="box"></span></div>
    <p class="ans">No, Supplement discounts are only for online purchases, in office supplements do not have discounts. We can however help you to make online purchases in the office if you are needing help.</p>
  </div>
  <div class="acc" style="top:355px"><div class="head">If we sign up for a couple's or family membership, are the membership benefits ?<span class="box"></span></div></div>
  <div class="acc" style="top:414px"><div class="head">Can I make changes to my membership package after I sign up?<span class="box"></span></div></div>
  <div class="acc" style="top:473px"><div class="head">If I choose not to join a package, will the level of care I receive be affected?<span class="box"></span></div></div>
</section>

<footer class="sitefoot">
  <div class="brand"><span class="dot"></span><span class="name">Bright Oak Clinic</span></div>
  <div class="social"><span></span><span></span><span></span><span></span><span></span></div>
  <h4 style="left:438px;top:40px">Hours</h4>
  <div class="hours">
    <div><span>Monday</span><span>8 am - 6 pm</span></div>
    <div><span>Tuesday</span><span>8 am - 6 pm</span></div>
    <div><span>Wednesday</span><span>9 am - 6 pm</span></div>
    <div><span>Thursday</span><span>8 am - 4 pm</span></div>
    <div><span>Friday</span><span>9 am - 1 pm</span></div>
    <p>The office is closed from 12-1 for lunch</p>
  </div>
  <h4 style="left:784px;top:40px">Get in Touch</h4>
  <div class="touch">
    <div><svg width="14" height="18" viewBox="0 0 14 18"><path fill="#bbb" d="M7 0a7 7 0 0 0-7 7c0 5 7 11 7 11s7-6 7-11a7 7 0 0 0-7-7zm0 10a3 3 0 1 1 0-6 3 3 0 0 1 0 6z"/></svg>2480 Linden Court Fairview, TX 75001</div>
    <div><svg width="16" height="16" viewBox="0 0 24 24"><path fill="#bbb" d="M6.6 10.8a15 15 0 0 0 6.6 6.6l2.2-2.2c.3-.3.7-.4 1-.2 1.1.4 2.3.6 3.6.6.6 0 1 .4 1 1V20c0 .6-.4 1-1 1A17 17 0 0 1 3 4c0-.6.4-1 1-1h3.5c.6 0 1 .4 1 1 0 1.3.2 2.5.6 3.6.1.3 0 .7-.2 1z"/></svg>(555) 214-7730</div>
    <div><svg width="16" height="16" viewBox="0 0 16 16"><rect x="1" y="5" width="14" height="9" fill="#bbb"/><rect x="4" y="1" width="8" height="5" fill="none" stroke="#bbb" stroke-width="1.5"/></svg>(555) 214-7731</div>
  </div>
</footer>

<div class="copyright">© Copyright 2018 Bright Oak Clinic . All Rights Reserved</div>

</body>
</html>
```